Web Design Project for Velopra cloud based service

None of us is a designer, and ENGLISH is not our first language, but we need to make sure that those bidding for this project understand that we're just looking for the creative components in order to build a website and we don't need you to create all the pages and /or diagram the website for us. Please ask as many questions as you want for us to ensure we don't waste your time.

Content and Community Management System
- We need a redesign of the Back Office Screens
o The kind of screen detailed on the (file 2 attached bellow) “Velopra Some Screens.pptx”
- Following, as a strong reference te velopra logo design line (file 1 attached bellow)
- We DO NOT need application, or implementation, only the following SOW.

Scope of Work (SOW) by components that we need:
- Main Theme
- Tables
- Buttons
- Icons
- Lists
- Form elements

OUT of Scope (we DO NOT need it):
· Emerging Windows implementation (jquery – lightbox)
· Layout (we do not need you to create the layout for us)
· Module Development (Css 3, jQuery, Html 5)

Reason: We're extending the deadline in order to have more options to select. The current option do not fit our expectation yet. Any question, please do it. Many thanks. Velopra Team.

Hi designers!

We've [a] extended the deadline in order to have more choices and we made a change on the Power Point file attached with [b] the 3 most important screen than include all the components/element we need designed from you.

We wait for your proposal.
Let's do it!

Many Thanks.
Best regards.

velopra Team.

```html
<!DOCTYPE html>
<html lang="en">
<head>
<meta charset="utf-8">
<title>Velopra – Back Office Theme</title>
<link rel="stylesheet" href="https://fonts.googleapis.com/css2?family=Roboto:wght@300;400;500;700&display=swap">
<style>
:root{
  --ink:#333333;
  --ink-soft:#555555;
  --muted:#8a8a8a;
  --bar:#232323;
  --bar-bottom:#333333;
  --brand-blue:#0b9bd7;
  --link-blue:#1ba5e0;
  --orange:#f26a10;
  --error:#c9302c;
  --line:#dddddd;
  --stripe:#f7f7f7;
  --panel:#ececec;
  --white:#ffffff;
}
*{box-sizing:border-box;margin:0;padding:0}
html,body{width:1200px;height:1096px;overflow:hidden}
body{position:relative;font-family:"Roboto",Arial,sans-serif;color:var(--ink);background:var(--white);font-size:12px}
.abs{position:absolute}

/* top bar */
.topbar{left:0;top:0;width:1200px;height:38px;background:var(--bar);border-bottom:1px solid #111}
.session{right:358px;top:12px;color:#eee;font-size:12px}
.session b{color:var(--link-blue);font-weight:500}
.pill{top:4px;height:30px;border-radius:15px;background:linear-gradient(#fafafa,#d6d6d6);color:#555;font-size:12px;display:flex;align-items:center;justify-content:center;border:1px solid #bbb}

/* header */
.header{left:0;top:39px;width:1200px;height:197px;background:linear-gradient(#ffffff,#f6f6f6 60%,#ececec);border-bottom:1px solid #e0e0e0}
.brand{left:126px;top:150px;font-size:26px;font-weight:700;color:#222;letter-spacing:0.5px}
.brand-mark{left:126px;top:78px;width:64px;height:64px;background:var(--brand-blue);border-radius:6px}
.nav-btn{top:115px;height:40px;border-radius:4px;background:linear-gradient(#ffffff,#f1f1f1);box-shadow:0 1px 3px rgba(0,0,0,.25);font-size:12px;font-weight:700;color:#999;display:flex;align-items:center;justify-content:center;gap:8px;text-transform:uppercase}
.nav-btn.active{background:var(--brand-blue);color:#fff}
.nav-btn.active::after{content:"";position:absolute;left:47px;bottom:-8px;border:8px solid transparent;border-bottom:0;border-top-color:var(--brand-blue)}
.nav-btn.hot{color:var(--orange)}
.nav-btn.open{height:56px;align-items:flex-start;padding-top:13px;border-radius:4px 4px 0 0;box-shadow:0 -1px 3px rgba(0,0,0,.15);z-index:2}
.subnav{left:516px;top:170px;width:192px;height:126px;background:linear-gradient(#ffffff,#f3f3f3);border-radius:0 4px 4px 4px;box-shadow:0 2px 4px rgba(0,0,0,.3);z-index:3;padding:0 20px}
.subnav li{list-style:none;height:41px;display:flex;align-items:center;gap:6px;color:#999;font-size:12px;font-weight:500;border-bottom:1px dotted #bbb}
.subnav li:last-child{border:0}
.subnav svg{flex:none}

/* content */
.h1{left:119px;top:288px;font-size:24px;font-weight:700}
.h2{left:119px;top:328px;font-size:18px;font-weight:700}
.body-copy{left:119px;top:354px;width:622px;font-size:12px;line-height:21px;color:var(--ink-soft)}
.body-copy a{color:var(--orange);font-weight:700;text-decoration:none;border-bottom:1px solid var(--orange)}

.data-table{left:120px;top:450px;width:622px;border-collapse:collapse;font-size:13px}
.data-table th{text-align:left;height:35px;font-weight:500;border-bottom:1px solid var(--line)}
.data-table td{height:35px;border-bottom:1px solid var(--line);color:#444}
.data-table tr:last-child td{border-bottom:0}
.data-table tbody tr:nth-child(odd){background:var(--stripe)}
.data-table .c1{padding-left:8px;width:73px}
.data-table .c2{width:234px}
.data-table .c3{width:230px}

.field-label{width:140px;text-align:right;font-size:13px;color:#444;left:118px}
.field-label.err{color:var(--error)}
.input{left:278px;height:28px;border:1px solid #ddd;border-radius:3px;font-size:13px;color:#555;padding:6px 6px;background:#fff}
.input.focus{border-color:#78b2e8;box-shadow:0 0 4px rgba(82,168,236,.6)}
.input.error{border-color:var(--error)}
.help-error{left:507px;top:741px;color:var(--error);font-size:13px}

.form-actions{left:118px;top:800px;width:624px;height:63px;background:#f5f5f5;border-top:1px solid #e3e3e3}
.btn{top:818px;height:28px;border-radius:4px;font-size:13px;display:flex;align-items:center;justify-content:center}
.btn.primary{left:278px;width:103px;background:linear-gradient(#0a88de,#0557c4);color:#fff;border:1px solid #0450a8}
.btn.plain{left:385px;width:62px;background:linear-gradient(#fff,#e6e6e6);color:#333;border:1px solid #ccc}

/* sidebar */
.sidebar{left:761px;top:283px;width:320px;height:288px;background:var(--panel);border-radius:8px;padding:24px 27px}
.sidebar h3{font-size:18px;font-weight:400;color:#333;text-transform:uppercase;margin-bottom:6px}
.sidebar ul{list-style:none}
.sidebar li{height:38px;display:flex;align-items:center;gap:6px;font-size:12px;font-weight:500;color:#333;border-bottom:1px dotted #999}
.sidebar li:last-child{border:0}

/* footer */
.footer{left:0;top:916px;width:1200px;height:148px;background:var(--brand-blue)}
.fcol{top:943px;color:#fff;font-size:12px;line-height:21px}
.fcol h4{font-size:12px;font-weight:700}
.fcol p{font-weight:300}
.foot-brand{left:1003px;top:1008px;color:#fff;font-weight:700;font-size:15px}
.bottombar{left:0;top:1064px;width:1200px;height:32px;background:var(--bar-bottom);color:#fff;font-size:11px;padding:8px 0 0 119px}
</style>
</head>
<body>

<div class="abs topbar"></div>
<div class="abs session">Loged in as <b>UserName</b></div>
<div class="abs pill" style="left:856px;width:137px">Change Password</div>
<div class="abs pill" style="left:1001px;width:76px">Log out</div>

<header class="abs header"></header>
<div class="abs brand">VELOPRA</div>

<div class="abs nav-btn active" style="left:390px;width:110px">Btn Active</div>
<div class="abs nav-btn open hot" style="left:516px;width:137px">With Sub-Nav</div>
<ul class="abs subnav">
  <li><svg width="11" height="11" viewBox="0 0 12 12"><path d="M6 1v5" stroke="#999" stroke-width="1.6"/><path d="M3.5 3a4 4 0 1 0 5 0" fill="none" stroke="#999" stroke-width="1.6"/></svg>SubNavigation link #1</li>
  <li><svg width="12" height="10" viewBox="0 0 12 10"><rect x="0" y="8" width="2" height="2" fill="#999"/><rect x="3" y="6" width="2" height="4" fill="#999"/><rect x="6" y="3" width="2" height="7" fill="#999"/><rect x="9" y="0" width="2" height="10" fill="#999"/></svg>SubNavigation link #2</li>
  <li><svg width="11" height="11" viewBox="0 0 12 12"><circle cx="6" cy="6" r="3.6" fill="none" stroke="#999" stroke-width="2.4" stroke-dasharray="2 1.4"/><circle cx="6" cy="6" r="2.6" fill="#999"/><circle cx="6" cy="6" r="1" fill="#fff"/></svg>SubNavigation link #3</li>
</ul>
<div class="abs nav-btn hot" style="left:657px;width:109px">Rollover</div>
<svg class="abs" style="left:753px;top:138px;z-index:4" width="24" height="32" viewBox="0 0 24 32"><path d="M2 1 L2 26 L8 20 L12 30 L16 28 L12 19 L21 19 Z" fill="#2a2a2a" stroke="#fff" stroke-width="1.2"/></svg>
<div class="abs nav-btn" style="left:781px;width:113px">Button #1</div>
<div class="abs nav-btn" style="left:906px;width:175px"><svg width="20" height="16" viewBox="0 0 20 16"><path d="M10 0 L20 8 L17 8 L17 16 L12 16 L12 11 L8 11 L8 16 L3 16 L3 8 L0 8 Z" fill="#999"/></svg>Button with icon</div>

<h1 class="abs h1">Headings &amp; body copy</h1>
<h2 class="abs h2">Typographic scale</h2>
<p class="abs body-copy">Sed egestas, ante et vulputate volutpat, eros pede semper est, vitae luctus metus libero eu augue. Morbi purus libero, faucibus adipiscing, commodo quis, gravida id, est. Sed lectus. Praesent elementum hendrerit tortor. Sed semper lorem at felis. Vestibulum volutpat, lacus a ultrices <a href="#">sagittis</a>, mi neque euismod dui, eu pulvinar nunc sapien ornare nisl. Phasellus pede arcu, dapibus eu, fermentum et, dapibus sed, urna.</p>

<table class="abs data-table">
  <thead><tr><th class="c1">#</th><th class="c2">First Name</th><th class="c3">Last Name</th><th>Username</th></tr></thead>
  <tbody>
    <tr><td class="c1">1</td><td>Mark</td><td>Orsen</td><td>@mor</td></tr>
    <tr><td class="c1">2</td><td>Jacob</td><td>Thorley</td><td>@jth</td></tr>
    <tr><td class="c1">3</td><td>Larry</td><td>the Finch</td><td>@larryf</td></tr>
  </tbody>
</table>

<label class="abs field-label" style="top:641px">Focused input</label>
<div class="abs input focus" style="top:635px;width:280px">This is focused…</div>
<label class="abs field-label" style="top:687px">Uneditable input</label>
<div class="abs input" style="top:681px;width:280px;background:#fdfdfd">Some value here</div>
<label class="abs field-label err" style="top:740px">Input with error</label>
<div class="abs input error" style="top:735px;width:220px"></div>
<span class="abs help-error">Please correct the error</span>

<div class="abs form-actions"></div>
<div class="abs btn primary">Save changes</div>
<div class="abs btn plain">Cancel</div>

<aside class="abs sidebar">
  <h3>Sidebar content</h3>
  <ul>
    <li><svg width="16" height="16" viewBox="0 0 16 16"><circle cx="8" cy="8" r="8" fill="#f26a10"/><path d="M8 4v8M4 8h8" stroke="#fff" stroke-width="2"/></svg>Sed egestas ante et vulputate volutpat</li>
    <li><svg width="16" height="16" viewBox="0 0 16 16"><circle cx="8" cy="8" r="8" fill="#f26a10"/><path d="M8 4v8M4 8h8" stroke="#fff" stroke-width="2"/></svg>Eros pede semper est, vitae luctus metus</li>
    <li><svg width="16" height="16" viewBox="0 0 16 16"><circle cx="8" cy="8" r="8" fill="#f26a10"/><path d="M8 4v8M4 8h8" stroke="#fff" stroke-width="2"/></svg>Libero eu augue. Morbi purus libero</li>
    <li><svg width="16" height="16" viewBox="0 0 16 16"><circle cx="8" cy="8" r="8" fill="#f26a10"/><path d="M8 4v8M4 8h8" stroke="#fff" stroke-width="2"/></svg>Faucibus adipiscing</li>
    <li><svg width="16" height="16" viewBox="0 0 16 16"><circle cx="8" cy="8" r="8" fill="#f26a10"/><path d="M8 4v8M4 8h8" stroke="#fff" stroke-width="2"/></svg>Commodo quis gravida id est.</li>
    <li><svg width="16" height="16" viewBox="0 0 16 16"><circle cx="8" cy="8" r="8" fill="#f26a10"/><path d="M8 4v8M4 8h8" stroke="#fff" stroke-width="2"/></svg>Sed lectus</li>
  </ul>
</aside>

<footer class="abs footer"></footer>
<div class="abs fcol" style="left:120px"><h4>Text of the link #1</h4><p>sublink a</p><p>sublink b</p><p>sublink c</p></div>
<div class="abs fcol" style="left:277px"><h4>Text of the link #2</h4><p>sublink a</p><p>sublink b</p></div>
<div class="abs fcol" style="left:433px"><h4>Text of the link #3</h4><p>sublink a</p><p>sublink b</p><p>sublink c</p><p>sublink d</p></div>
<div class="abs fcol" style="left:590px"><h4>Text of the link #4</h4><p>sublink a</p><p>sublink b</p><p>sublink c</p></div>
<div class="abs foot-brand">VELOPRA</div>
<div class="abs bottombar">© copyright 2012 Velopra. All Rights Reserved</div>

</body>
</html>
```